Brindlewave Systems Website Project

We require a design to revamp and existing website for a company that provides online solutions for small the medium sized businesses including web development, online marketing, social media, online business plans, social media and e-commerce. We are looking to use colours that integrate well with the current logo. Our target market are small to medium sized businesses and individuals looking for a trusted adviser to cover all their online services.
Existing website - www.brindlewavesystems.com.au
Updates
Participation payments added.
Storyboard layout mentioned in brief was not attached in error. It will be uploaded shortly.
Storyboard file added.
Target Market(s)
Revamp of existing website - Looking for a professional design in line with the target market of small to medium businesses
Industry/Entity Type
Business
Requirements
Must have
- Refer the attached storyboard layout for the site design and requirements. Basic header, footer and sidebar are to be the same on every page with the content changing to match the requirements on each page. 8 pages in total
Should not have
- No click here text

```html
<!DOCTYPE html>
<html lang="en">
<head>
<meta charset="utf-8">
<title>Brindlewave Systems – Leading the way in Online Solutions</title>
<link rel="stylesheet" href="https://fonts.googleapis.com/css2?family=Source+Sans+3:wght@400;600;700&family=Arimo:wght@400;700&display=swap">
<style>
:root{
  --page:#ececec;
  --white:#ffffff;
  --green:#5bb43a;
  --green-dark:#3f8d22;
  --charcoal:#333333;
  --ink:#444444;
  --body:#555555;
  --muted:#888888;
  --line:#cfcfcf;
  --band:#b9bcbd;
  --hero-a:#e9e4df;
  --hero-b:#c9bdb4;
}
*{box-sizing:border-box;margin:0;padding:0}
html,body{width:1029px;height:1200px;overflow:hidden}
body{background:radial-gradient(ellipse at 50% 30%,#f7f7f7 0%,var(--page) 70%);font-family:"Arimo",Arial,sans-serif;color:var(--body);position:relative}
.abs{position:absolute}
.brand{left:108px;top:0;width:184px;height:157px;background:var(--charcoal);display:flex;flex-direction:column;align-items:center;justify-content:center;gap:10px;z-index:3}
.brand-dot{width:58px;height:58px;border-radius:50%;background:var(--white)}
.brand-name{font-family:"Source Sans 3",sans-serif;font-weight:600;font-size:21px;color:var(--white);text-align:center;line-height:1.05}
.utility{right:94px;top:10px;font-size:11px;color:var(--ink);display:flex;gap:8px}
.utility span.sep{color:var(--line)}
.tagline{left:329px;top:34px;font-family:"Source Sans 3",sans-serif;font-size:19px;color:#6a6a6a}
.search{left:641px;top:33px;width:287px;height:26px;background:var(--white);border:1px solid #cfcfcf;border-left:3px solid #bbb;border-right:3px solid #bbb;font-size:10px;font-style:italic;color:#9a9a9a;padding:6px 8px;letter-spacing:.3px}
.search svg{position:absolute;right:6px;top:3px}
.hero{left:107px;top:73px;width:809px;height:255px;background:var(--white);box-shadow:0 10px 10px -6px rgba(0,0,0,.35)}
.hero-photo{position:absolute;left:0;top:0;width:480px;height:255px;background:linear-gradient(180deg,#fafafa 0%,var(--hero-a) 55%,var(--hero-b) 100%)}
.hero-copy{position:absolute;left:466px;top:12px;font-family:"Source Sans 3",sans-serif}
.hero-copy h1{font-size:33px;line-height:35px;font-weight:700;color:var(--green)}
.hero-copy h1 em{font-style:normal;color:#555}
.hero-copy p{margin-top:6px;font-size:21px;line-height:24px;color:var(--green)}
.dots{left:486px;top:333px;display:flex;gap:4px}
.dots i{width:11px;height:11px;border-radius:50%;background:var(--charcoal)}
.dots i.on{background:var(--green)}
.nav{left:97px;top:352px;width:838px;height:62px;background:var(--white);border:1px solid #dcdcdc;display:flex;align-items:center;justify-content:center;font-size:13.5px;color:#666}
.nav a{color:inherit;text-decoration:none;padding:0 18px;border-left:1px dotted #bbb}
.nav a:first-child{border-left:0;color:var(--green)}
.band{left:97px;width:838px;height:16px}
.main{left:97px;top:436px;width:838px;height:640px;background:var(--white);border:1px solid #d2d2d2}
.title{font-family:"Source Sans 3",sans-serif;font-weight:700;font-size:28px;color:var(--charcoal);white-space:nowrap}
.title b{color:var(--green)}
.welcome{left:22px;top:14px}
.intro{left:22px;top:58px;width:490px;font-size:12.4px;line-height:18.2px}
.rule{left:20px;top:174px;width:497px;border-top:1px dotted #aaa}
.vrule{left:545px;top:24px;height:456px;border-left:1px dotted #aaa}
.card{width:154px;height:131px;background:var(--white);border:5px solid #ddd;box-shadow:0 2px 3px rgba(0,0,0,.3)}
.card h3{background:var(--charcoal);color:var(--green);font-family:"Source Sans 3",sans-serif;font-weight:700;font-size:14px;letter-spacing:-.1px;padding:6px 6px;height:29px;white-space:nowrap;overflow:hidden}
.card p{font-size:10.5px;line-height:13.4px;padding:4px 12px 0 7px;color:#555}
.more{position:absolute;left:7px;bottom:5px;width:66px;height:24px;border-radius:12px;background:linear-gradient(#7bc653,var(--green-dark));border:2px solid var(--charcoal);color:var(--white);font-size:10.5px;font-weight:700;display:flex;align-items:center;justify-content:center}
.why{left:588px;top:14px}
.why-list{left:587px;top:58px;list-style:none;font-size:11px;line-height:15.9px;color:#555;width:240px}
.why-rule{left:587px;top:206px;width:228px;border-top:1px dotted #aaa}
.quote{left:573px;top:220px;width:254px;height:259px;background:var(--charcoal)}
.quote h2{position:absolute;left:31px;top:6px;font-family:"Source Sans 3",sans-serif;font-weight:700;font-size:19px;color:var(--green)}
.field{position:absolute;left:30px;width:194px;height:24px;background:var(--white);font-size:11px;color:#999;padding:5px 4px}
.submit{position:absolute;left:30px;top:227px;width:104px;height:19px;background:linear-gradient(#6cc043,var(--green-dark));color:var(--white);font-family:"Source Sans 3",sans-serif;font-weight:700;font-size:17px;line-height:19px;padding-left:20px}
.carousel{left:110px;top:936px;width:814px;height:117px;background:var(--white);border:5px solid #f0f0f0;box-shadow:0 10px 10px -6px rgba(0,0,0,.3)}
.thumb{position:absolute;top:12px;width:118px;height:89px;border:3px solid #ddd;box-shadow:0 1px 3px rgba(0,0,0,.3)}
.arrow{width:28px;height:28px;border-radius:50%;background:linear-gradient(#fafafa,#cfcfcf);border:1px solid #aaa;display:flex;align-items:center;justify-content:center}
.social{left:428px;top:1088px;display:flex;gap:17px}
.social i{width:28px;height:28px;border-radius:4px;background:linear-gradient(#f8f8f8,#d8d8d8);border:1px solid #c5c5c5}
.footer{left:97px;top:1128px;width:838px;height:64px;background:var(--white);border:1px solid #dcdcdc;font-size:11px;color:#333;text-align:center;padding-top:32px}
</style>
</head>
<body>
<div class="abs brand"><span class="brand-dot"></span><span class="brand-name">Brindlewave<br>Systems</span></div>
<div class="abs utility"><span>HOME</span><span class="sep">⁝</span><span>SITE-MAP</span><span class="sep">⁝</span><span>CONTACT</span></div>
<div class="abs tagline">Leading the way in Online Solutions</div>
<div class="abs search">TYPE YOUR KEYWORDS...
  <svg width="20" height="20" viewBox="0 0 20 20"><circle cx="8" cy="8" r="6" fill="none" stroke="#999" stroke-width="2.5"/><line x1="12.5" y1="12.5" x2="18" y2="18" stroke="#999" stroke-width="3"/></svg>
</div>

<div class="abs hero">
  <div class="hero-photo" role="img" aria-label="Photo of a smiling businesswoman in front of a row of colleagues"></div>
  <div class="hero-copy">
    <h1>Make navigating your<br><em>business online easy</em></h1>
    <p>We provide ongoing service<br>ensure we are delivering the<br>best solution for your business</p>
  </div>
</div>
<div class="abs dots"><i class="on"></i><i></i><i></i><i></i></div>

<nav class="abs nav"><a>HOME</a><a>ABOUT</a><a>TECHNOLOGY</a><a>SERVICE</a><a>BLOG</a><a>PORTFOLIO</a><a>ADVANTAGES</a><a>CONTACT US</a></nav>
<svg class="abs band" style="top:414px" viewBox="0 0 838 16" preserveAspectRatio="none"><path d="M0 0H838V16Q419 4 0 16Z" fill="#b9bcbd"/></svg>

<main class="abs main">
  <h2 class="abs title welcome">Welcome To <b>Our Site!</b></h2>
  <p class="abs intro">Lorem ipsum dolor sit amet, consectetuer adipiscing elit, sed diam nonummy nibh euismod tincidunt ut laoreet dolore magna aliquam erat volutpat. Ut wisi enim ad minim veniam, quis nostrud exerci tation ullamcorper suscipit lobortis nisl ut aliquip ex ea commodo consequat. Duis autem vel eum iriure dolor in hendrerit in vulputate velit esse molestie consequat, vel illum dolore eu feugiat nulla facilisis at vero eros et accumsan et iusto odio dignissim.</p>
  <div class="abs rule"></div>

  <div class="abs card" style="left:20px;top:192px"><h3>BLOG</h3><p>Need a dynamic blog to compliment your business or want a blog for personal expression?</p><span class="more">Read more..</span></div>
  <div class="abs card" style="left:191px;top:192px"><h3>SOCIAL MEDIA</h3><p>Need a dynamic blog to compliment your business or want a blog for personal expression?</p><span class="more">Read more..</span></div>
  <div class="abs card" style="left:361px;top:192px"><h3>DEVELOPMENT</h3><p>Need a dynamic blog to compliment your business or want a blog for personal expression?</p><span class="more">Read more..</span></div>
  <div class="abs card" style="left:20px;top:346px"><h3>E-COMMERCE</h3><p>Need a dynamic blog to compliment your business or want a blog for personal expression?</p><span class="more">Read more..</span></div>
  <div class="abs card" style="left:191px;top:346px"><h3>ONLINE BUSINESS</h3><p>Need a dynamic blog to compliment your business or want a blog for personal expression?</p><span class="more">Read more..</span></div>
  <div class="abs card" style="left:361px;top:346px"><h3>ONLINE MARKETING</h3><p>Need a dynamic blog to compliment your business or want a blog for personal expression?</p><span class="more">Read more..</span></div>

  <div class="abs vrule"></div>
  <h2 class="abs title why"><b>Why Choose Us?</b></h2>
  <ul class="abs why-list">
    <li>Website solutions tailored to your business</li>
    <li>Cost effective pricing to suit your budget</li>
    <li>Strategies to support your online presence</li>
    <li>Regular maintenance packages available</li>
    <li>Professional design and development</li>
    <li>Online business plans to promote growth</li>
    <li>SEO techniques incorporated into all solutions</li>
    <li>Online marketing options available</li>
    <li>Blogs and e-commerce solutions available</li>
  </ul>
  <div class="abs why-rule"></div>

  <form class="abs quote">
    <h2>Request a Quote</h2>
    <div class="field" style="top:38px">BUSINESS NAME:</div>
    <div class="field" style="top:70px">EMAIL:</div>
    <div class="field" style="top:101px">PHONE NUMBER:</div>
    <div class="field" style="top:133px;height:85px"></div>
    <div class="submit">SUBMIT</div>
  </form>
</main>

<div class="abs carousel">
  <div class="thumb" role="img" aria-label="Portfolio website preview" style="left:24px;background:#cfe6c0"></div>
  <div class="thumb" role="img" aria-label="Portfolio website preview" style="left:182px;background:linear-gradient(#f0c9a8 0 14px,#fff 14px)"></div>
  <div class="thumb" role="img" aria-label="Portfolio website preview" style="left:343px;background:linear-gradient(90deg,#f2f2f2 30%,#dcdcdc 30% 70%,#f2f2f2 70%)"></div>
  <div class="thumb" role="img" aria-label="Portfolio website preview" style="left:499px;background:linear-gradient(#fff 10px,#f5e9a0 10px 16px,#fafafa 16px 60px,#777 60px)"></div>
  <div class="thumb" role="img" aria-label="Portfolio website preview" style="left:658px;background:#bfe0b0"></div>
</div>
<div class="abs arrow" style="left:103px;top:982px"><svg width="10" height="12" viewBox="0 0 10 12"><path d="M8 1 3 6l5 5" fill="none" stroke="#444" stroke-width="2.5"/></svg></div>
<div class="abs arrow" style="left:900px;top:982px"><svg width="10" height="12" viewBox="0 0 10 12"><path d="M2 1l5 5-5 5" fill="none" stroke="#444" stroke-width="2.5"/></svg></div>

<div class="abs social" aria-label="Social links"><i></i><i></i><i></i><i></i></div>
<svg class="abs band" style="top:1112px" viewBox="0 0 838 16" preserveAspectRatio="none"><path d="M0 16H838V0Q419 12 0 0Z" fill="#b9bcbd"/></svg>
<footer class="abs footer">All Contents © Copyright Brindlewave Systems,2012. All Rights Reserved. Terms of Use | Privacy</footer>
</body>
</html>
```